Pella Acupuncture Business Card Design

I would like a business card design for my acupuncture business which is based from 2 practices in Melbourne, Australia.

The front of the card should include:

*The Logo
* Name - Miranda Tovelisca (B.App.Sc.(TCM), Dip.Rem.Mass.). (I would like the letters after my name in slightly smaller font)
* Mobile number - 0472 318 604
* Web address - www.pellaacupuncture-example.com.au

On the back of the card I would somehow like to fit my 2 clinic addresses in. They are:

The Birchwood Restoration Rooms
842 Fennimore Rd, Camberwell VIC 3124
Ph: 1300 274 518

Quillbrook Integrative & Eastern Herbal Therapy Clinic
31 Marlowby Rd, Malvern East VIC 3145
Ph: (03) 9871 3352

If there is space, I'd also like to add to the back of the card - Next Appointment............................ (or something along those lines).

Thanks and happy designing!

Target Market(s)

Health consumers, and colleagues in the health industry

Industry/Entity Type

Clinic

Contact Information for Business Card

as above in brief

Requirements
Must have
• I've seen some ok designs coming in, however I'd like to avoid the generic look with the added curved line details etc. I don't particularly need extra patterns added to the card. I'd prefer it to look quite clean and simple, and using more earthy colours (I'm not super keen on the lime green that a lot of designs seem to include. I don't mind the full black or white look, (obviously the back side needs to be a lighter colour to allow me to write appointment details on it). I also quite like the idea of the background looking like brown recycled paper (just an idea - that's not 100% necessary).
Nice to have
• I have an idea that I could have the main flower part of the logo printed as metallic.
Should not have
• Generic patterns and too much added detail.

```html
<!DOCTYPE html>
<html lang="en">
<head>
<meta charset="utf-8">
<title>Pella Acupuncture – Business Card</title>
<link rel="stylesheet" href="https://fonts.googleapis.com/css2?family=Cormorant+Garamond:wght@500;600&family=Open+Sans:wght@400;600;700&display=swap">
<style>
  :root {
    --page: #ecebe8;
    --card-light: #ffffff;
    --card-dark: #0d1112;
    --card-dark-edge: #1a2224;
    --ink: #3a3a3a;
    --ink-strong: #1f1f1f;
    --ink-soft: #6b6b6b;
    --rule: #4a4a4a;
    --on-dark: #f2f2f2;
    --accent: #b9b98a;
  }
  * { box-sizing: border-box; margin: 0; padding: 0; }
  html, body {
    width: 1200px; height: 800px; overflow: hidden;
    background: var(--page);
  }
  .canvas {
    width: 1200px; height: 800px;
    display: flex; align-items: center; justify-content: center; gap: 60px;
  }
  .card {
    width: 520px; height: 298px;
    border-radius: 3px;
    box-shadow: 0 6px 18px rgba(0,0,0,.18);
    position: relative; overflow: hidden;
  }

  /* Back of card */
  .card-back {
    background: var(--card-light);
    color: var(--ink);
    font-family: "Open Sans", Arial, sans-serif;
    padding: 26px 28px;
  }
  .appointment {
    font-size: 12px; color: var(--ink-soft);
  }
  .appointment-title { margin-bottom: 6px; }
  .appointment-fields { display: flex; gap: 16px; align-items: flex-end; }
  .field { display: flex; align-items: flex-end; gap: 6px; }
  .field-line { border-bottom: 1px solid var(--rule); height: 14px; }
  .field-date .field-line { width: 200px; }
  .field-time .field-line { width: 150px; }

  .clinics {
    margin-top: 22px;
    display: flex; flex-direction: column; gap: 16px;
    width: 300px;
    font-size: 11.5px; line-height: 1.45;
  }
  .clinic-name { font-weight: 700; color: var(--ink-strong); }
  .clinic-phone { display: flex; align-items: center; gap: 6px; }
  .clinic-phone svg { width: 11px; height: 11px; }

  .brand {
    position: absolute; right: 28px; bottom: 34px;
    display: flex; flex-direction: column; align-items: center; gap: 10px;
  }
  .brand-dot {
    width: 96px; height: 96px; border-radius: 50%;
    background: var(--card-dark);
  }
  .brand-name {
    font-family: "Open Sans", Arial, sans-serif;
    font-size: 13px; font-weight: 600; color: var(--ink-strong);
    letter-spacing: .06em;
  }

  /* Front of card */
  .card-front {
    background: var(--card-dark);
    color: var(--on-dark);
    display: flex; flex-direction: column; align-items: center; justify-content: center;
    text-align: center;
  }
  .front-backdrop {
    position: absolute; inset: 0;
    background: radial-gradient(circle at 50% 55%, var(--card-dark-edge) 0, var(--card-dark-edge) 38%, var(--card-dark) 72%);
  }
  .practitioner { position: relative; }
  .practitioner-name {
    font-family: "Cormorant Garamond", Georgia, serif;
    font-variant: small-caps;
    font-weight: 600; font-size: 24px; letter-spacing: .04em;
  }
  .qualifications {
    font-size: 17px; font-variant: normal; letter-spacing: 0;
  }
  .contact {
    position: relative; margin-top: 22px;
    font-family: "Open Sans", Arial, sans-serif;
    font-size: 12.5px; line-height: 1.6;
  }
</style>
</head>
<body>
<main class="canvas">

  <section class="card card-back" aria-label="Back of business card">
    <div class="appointment">
      <p class="appointment-title">Next Appointment</p>
      <div class="appointment-fields">
        <span class="field field-date">Date: <span class="field-line"></span></span>
        <span class="field field-time">Time: <span class="field-line"></span></span>
      </div>
    </div>

    <div class="clinics">
      <div class="clinic">
        <p class="clinic-name">Quillbrook Integrative &amp; Eastern Herbal Therapy Clinic</p>
        <p>31 Marlowby Rd, Malvern East VIC 3145</p>
        <p class="clinic-phone">
          <svg viewBox="0 0 12 12" aria-hidden="true"><rect width="12" height="12" rx="2" fill="#3a3a3a"/><path d="M4 3l1.2 1.6-.7.8a4 4 0 0 0 2.1 2.1l.8-.7L9 8l-.6 1.2C6 9 3 6 2.8 3.6z" fill="#fff"/></svg>
          (03) 9871 3352
        </p>
      </div>
      <div class="clinic">
        <p class="clinic-name">The Birchwood Restoration Rooms</p>
        <p>842 Fennimore Rd, Camberwell VIC 3124</p>
        <p class="clinic-phone">
          <svg viewBox="0 0 12 12" aria-hidden="true"><rect width="12" height="12" rx="2" fill="#3a3a3a"/><path d="M4 3l1.2 1.6-.7.8a4 4 0 0 0 2.1 2.1l.8-.7L9 8l-.6 1.2C6 9 3 6 2.8 3.6z" fill="#fff"/></svg>
          1300 274 518
        </p>
      </div>
    </div>

    <div class="brand">
      <span class="brand-dot" aria-hidden="true"></span>
      <span class="brand-name">Pella Acupuncture</span>
    </div>
  </section>

  <section class="card card-front" aria-label="Front of business card">
    <div class="front-backdrop" role="img" aria-label="Faint dark background decoration"></div>
    <h1 class="practitioner practitioner-name">Miranda Tovelisca <span class="qualifications">(B.App.Sc.(TCM), Dip.Rem.Mass.)</span></h1>
    <div class="contact">
      <p>0472 318 604</p>
      <p>www.pellaacupuncture-example.com.au</p>
    </div>
  </section>

</main>
</body>
</html>
```